Business Cards + Flyer + Letterhead for Care Recruitment Agency

We are a recruitment agency for the health & care sector. We need designs made for business cards, A5 double-sided flyer, and a letterhead template.

Our branding message is professionalism, care, compassion, expertise. We are experts in recruitment for the care & health industry.

Our logo source files and colours are here - https://www.fileporta.net/sh/qrvn82lopx4kdte/BBBgKy8LMQ27uTnPwZxHcVobsa?dl=0

For the business card, I have attached an example we like. We want a vertical business card design, something very similar to the example given. The design should match our logo in terms of brand colors. On one side should be our logo, our website (www.hollowmere.co.uk) and Care Recruitment Specialists written somewhere visible that fits, between our logo and the website at the bottom. On the other side should be our details.

Details on the front:

Logo with slogan
Care Recruitment Specialists
www.hollowmere.co.uk

Details on the back:

Tobias Orlund
Managing Director

Pellam House, 31-39 Larkfield St, Birmingham, B4 7QD
07612 495371
tobias@hollowmere.co.uk
www.hollowmere.co.uk

Marnie Holloway
Business Development Director

07831 204968
marnie@hollowmere.co.uk
www.hollowmere.co.uk

For the A5 flyer, I have attached some pictures we've used for the website, which could be used for the flyer as well. To get a better idea of our branding, please visit our website - https://hollowmere.co.uk/

The text for the flyer is also attached.

Finally, the letterhead template should be a docx template with our logo and our identifiable branding (the same shapes and matching colours you will come up with for the business cards and flyer).

```html
<!DOCTYPE html>
<html lang="en">
<head>
<meta charset="utf-8">
<title>Hollowmere — Stationery Set</title>
<link href="https://fonts.googleapis.com/css2?family=Open+Sans:wght@400;600&family=Roboto:wght@400;700&display=swap" rel="stylesheet">
<style>
  :root {
    --navy: #0c2a6e;
    --navy-deep: #0a2260;
    --royal: #13399a;
    --sky: #1a9bf0;
    --cyan: #19c3f0;
    --ink: #333a45;
    --grey-text: #555c66;
    --rule: #9aa3b2;
    --paper: #ffffff;
    --stage: #e6e7e9;
  }
  * { margin: 0; padding: 0; box-sizing: border-box; }
  html, body { width: 1200px; height: 1000px; overflow: hidden; }
  body { background: var(--stage); position: relative; font-family: "Open Sans", sans-serif; }

  /* ---------- Company name ---------- */
  .brand { text-align: center; }
  .brand__name { font-weight: 600; color: var(--navy); line-height: 1; letter-spacing: .04em; }

  /* ---------- Letterhead ---------- */
  .letterhead {
    position: absolute; left: 100px; top: 233px; width: 464px; height: 594px;
    background: var(--paper); box-shadow: 0 4px 14px rgba(0,0,0,.18);
  }
  .letterhead__bar {
    height: 6px; background: linear-gradient(90deg, var(--sky), var(--cyan) 55%, var(--sky));
  }
  .letterhead .brand { margin-top: 24px; }
  .letterhead .brand__name { font-family: "Open Sans", sans-serif; font-size: 15px; }

  .letter {
    position: absolute; left: 43px; top: 108px; width: 376px;
    font-size: 7.4px; color: var(--grey-text); line-height: 1.25;
  }
  .letter p { margin-bottom: 10px; }
  .letter .letter__date { margin-bottom: 9px; }
  .letter .letter__recipient { margin-bottom: 18px; }
  .letter .letter__body { line-height: 13.3px; text-align: justify; margin-bottom: 13px; }
  .letter .letter__close { margin-top: 20px; margin-bottom: 8px; }
  .letter__signature {
    width: 108px; height: 14px; border-radius: 3px;
    background: linear-gradient(90deg, #eceef2, #f6f7f9);
    margin-bottom: 8px;
  }
  .letter__signer { font-size: 9px; color: var(--ink); }
  .letter__role { margin-top: 3px; }

  .letterhead__footer {
    position: absolute; left: 0; bottom: 0; width: 100%; height: 43px;
    background: linear-gradient(180deg, var(--royal), var(--navy-deep));
    color: #fff; text-align: center; font-size: 8.6px; padding-top: 9px;
  }
  .footer__address {
    display: inline-block; width: 320px; padding-bottom: 3px;
    border-bottom: 1px solid rgba(255,255,255,.45);
  }
  .footer__contact { margin-top: 3px; }
  .letterhead__footer b { font-weight: 600; }

  /* ---------- Business cards ---------- */
  .card {
    position: absolute; top: 394px; width: 245px; height: 397px;
    box-shadow: 0 4px 12px rgba(0,0,0,.22);
    font-family: "Roboto", sans-serif;
  }
  .card--front { left: 620px; background: var(--navy); overflow: hidden; }
  .card__pattern {
    position: absolute; inset: 0;
    background: linear-gradient(180deg, #173fa8 0%, #12338b 55%, #0c2766 100%);
  }
  .card--front .brand { position: absolute; left: 0; right: 0; top: 172px; }
  .card--front .brand__name { font-family: "Roboto", sans-serif; font-weight: 400; font-size: 16px; color: var(--sky); }
  .card__tagline {
    position: absolute; left: 0; right: 0; top: 336px; text-align: center;
    font-size: 10px; color: var(--sky);
  }

  .card--back { left: 886px; width: 243px; background: var(--paper); text-align: center; color: #222; }
  .card--back .brand { position: absolute; left: 0; right: 0; top: 90px; }
  .card--back .brand__name { font-family: "Roboto", sans-serif; font-weight: 700; font-size: 16px; }
  .contact__name {
    position: absolute; left: 0; right: 0; top: 215px;
    font-weight: 700; font-size: 17px; color: var(--navy);
  }
  .contact__role { position: absolute; left: 0; right: 0; top: 236px; font-size: 11px; }
  .contact__icons {
    position: absolute; left: 58px; right: 58px; top: 256px; height: 17px;
    display: flex; align-items: center; justify-content: center; gap: 3px;
  }
  .contact__icons::before, .contact__icons::after { content: ""; flex: 1; height: 1px; background: var(--rule); }
  .contact__icons::before { margin-right: 6px; }
  .contact__icons::after { margin-left: 6px; }
  .icon { width: 16px; height: 16px; background: var(--navy); border-radius: 2px; display: flex; align-items: center; justify-content: center; }
  .contact__lines { position: absolute; left: 0; right: 0; top: 280px; font-size: 11px; line-height: 14.5px; }
  .contact__lines .web-domain { color: var(--navy); }
  .contact__rule { position: absolute; left: 59px; right: 59px; top: 330px; height: 1px; background: var(--rule); }
  .contact__address { position: absolute; left: 0; right: 0; top: 340px; font-size: 11px; line-height: 14.5px; }
</style>
</head>
<body>

<section class="letterhead" aria-label="Letterhead">
  <div class="letterhead__bar"></div>
  <header class="brand"><div class="brand__name">HOLLOWMERE</div></header>

  <article class="letter">
    <p class="letter__date">Issuing Date: May 5, 2018</p>
    <p class="letter__recipient">Name Of Employee Mr. XYZABC<br>Address of Employee<br>Address Line 2 etc..</p>
    <p>Dear Mr.XYZABC</p>
    <p class="letter__body">Lorem Ipsum has been the industry's standard dummy text ever since the 1500s, when an unknown printer took a galley of type and scrambled it to make a type specimen book. It has survived not only five centuries, but also the leap into electronic typesetting, remaining essentially unchanged. It was popularised in the 1960s with the release of Lettrafold sheets containing Lorem Ipsum passages, and more recently with desktop publishing software like Pressmark Layout including versions of Lorem Ipsum.</p>
    <p class="letter__body">Lorem Ipsum is simply dummy text of the printing and typesetting industry. Lorem Ipsum has been the industry's standard dummy text ever since the 1500s, when an unknown printer took a galley of type and scrambled it to make a type specimen book.</p>
    <p class="letter__body">It has survived not only five centuries, but also the leap into electronic typesetting, remaining essentially unchanged. It was popularised in the 1960s with the release of Lettrafold sheets containing Lorem Ipsum passages.</p>
    <p class="letter__close">Yours Sincerely</p>
    <div class="letter__signature" role="img" aria-label="Handwritten signature of Edwin Marlow"></div>
    <div class="letter__signer">Edwin Marlow</div>
    <div class="letter__role">Managing Director</div>
  </article>

  <footer class="letterhead__footer">
    <div class="footer__address">Pellam House, 31-39 Larkfield St Birmingham, B4 7QD</div>
    <div class="footer__contact"><b>P:</b> 07612 495371 | <b>E:</b> tobias@hollowmere.co.uk | www.hollowmere.co.uk</div>
  </footer>
</section>

<section class="card card--front" aria-label="Business card front">
  <div class="card__pattern" role="img" aria-label="Repeating embossed pattern in deep blue"></div>
  <div class="brand"><div class="brand__name">HOLLOWMERE</div></div>
  <div class="card__tagline">CARE RECRUITMENT SPECIALISTS</div>
</section>

<section class="card card--back" aria-label="Business card back">
  <header class="brand"><div class="brand__name">HOLLOWMERE</div></header>
  <div class="contact__name">TOBIAS ORLUND</div>
  <div class="contact__role">Managing Director</div>
  <div class="contact__icons">
    <span class="icon"><svg width="11" height="11" viewBox="0 0 24 24"><path fill="#fff" d="M6.6 10.8a15 15 0 0 0 6.6 6.6l2.2-2.2c.3-.3.7-.4 1-.2 1.1.4 2.3.6 3.6.6.6 0 1 .4 1 1V20c0 .6-.4 1-1 1A17 17 0 0 1 3 4c0-.6.4-1 1-1h3.5c.6 0 1 .4 1 1 0 1.3.2 2.5.6 3.6.1.3 0 .7-.2 1z"/></svg></span>
    <span class="icon"><svg width="11" height="11" viewBox="0 0 24 24"><rect x="2" y="5" width="20" height="14" rx="1" fill="none" stroke="#fff" stroke-width="2"/><path d="M2 6l10 7 10-7" fill="none" stroke="#fff" stroke-width="2"/></svg></span>
    <span class="icon"><svg width="11" height="11" viewBox="0 0 24 24"><circle cx="12" cy="12" r="9" fill="none" stroke="#fff" stroke-width="2"/><path d="M3 12h18M12 3c3 3 3 15 0 18M12 3c-3 3-3 15 0 18" fill="none" stroke="#fff" stroke-width="1.6"/></svg></span>
  </div>
  <div class="contact__lines">
    07612 495371<br>
    tobias@hollowmere.co.uk<br>
    www.<span class="web-domain">hollowmere</span>.co.uk
  </div>
  <div class="contact__rule"></div>
  <div class="contact__address">Pellam House, 31-39 Larkfield St<br>Birmingham, B4 7QD</div>
</section>

</body>
</html>
```